Design layout of business card

Create a business card using existing logo and company information.
Our newly established business provides advice to family owned businesses for their succession planning, value improvement and also on business sales and acquisitions.

Target Market(s)

Owners of family businesses

Contact Information for Business Card

Key contact details are:
Greg Holloway
Director
P: 08 9342 5817
W: 0431 587 209
Address: Unit 4, 15 Kestrel Lane, Dunsborough, WA, 6281
Website: kinventureadvisory.com.au
Email: greg@kinventureadvisory.com.au

In smaller font somewhere needs to be these details:
ABN: 47 219 583 906
Licensed Real Estate & Business Agent No. RA53174
QTN Licensee Services Pty Ltd
AFSL No. 527361

Font styles to use
Sans Serif

Requirements
Must have
• Kin Venture Advisory logo to feature on front.
• Remaining logos to be included smaller and on back.
• Orla Business Sales logo to have words 'Powered by' next to it and to be the first of the uploaded logo files.
• Colours on card should complement the logo
Nice to have
• Clear and clean layout
• Logos for contact details for conciseness e.g. phone icon for mobile

```html
<!DOCTYPE html>
<html lang="en">
<head>
<meta charset="utf-8">
<title>Kin Venture Advisory – Business Card</title>
<link href="https://fonts.googleapis.com/css2?family=Lato:wght@700;900&family=Montserrat:wght@500&display=swap" rel="stylesheet">
<style>
  :root {
    --backdrop: #dfe0df;
    --card: #ffffff;
    --orange: #e85c2b;
    --grey: #a0a4a8;
    --faint-grey: #ecedef;
    --ink: #111111;
    --navy: #23418a;
    --teal: #1c7a9c;
  }
  html, body {
    margin: 0;
    width: 1200px;
    height: 1200px;
    overflow: hidden;
    background: var(--backdrop);
  }
  .card {
    position: absolute;
    left: 197px;
    width: 805px;
    height: 460px;
    background: var(--card);
    overflow: hidden;
    box-shadow: 4px 5px 8px rgba(0,0,0,0.15);
    font-family: "Lato", sans-serif;
  }
  .card--front { top: 107px; }
  .card--back { top: 632px; }
  .abs { position: absolute; margin: 0; }

  .brand-ring { position: absolute; }
  .brand-name {
    position: absolute;
    font-family: "Lato", sans-serif;
    font-weight: 900;
    font-size: 43px;
    line-height: 44px;
    color: var(--orange);
    letter-spacing: 0.3px;
  }
  .front-brand-ring { left: 47px; top: 25px; }
  .front-brand-name { left: 218px; top: 38px; }
  .back-brand-ring { left: 216px; top: 24px; }
  .back-brand-name { left: 388px; top: 32px; }

  .deco-ring { position: absolute; left: 345px; top: 0; }

  .holder-name {
    left: 47px; top: 236px;
    font-size: 32px; font-weight: 900; color: var(--orange);
  }
  .holder-role {
    left: 48px; top: 279px;
    font-size: 15px; font-weight: 700; color: var(--ink);
  }
  .divider {
    left: 50px; top: 303px;
    width: 710px; height: 3px;
    background: var(--orange);
  }
  .contact-list {
    left: 46px; top: 346px;
    list-style: none; padding: 0;
  }
  .contact-list li {
    display: flex; align-items: center;
    height: 22.5px;
    font-size: 15.5px; font-weight: 700; color: var(--ink);
    letter-spacing: 1.6px;
  }
  .contact-list li.email { letter-spacing: 0.8px; }
  .contact-list svg { width: 15px; height: 15px; margin-right: 13px; flex: none; }
  .address {
    right: 45px; top: 346px;
    text-align: right;
    font-style: normal;
    font-size: 15.5px; font-weight: 700; color: var(--ink);
    line-height: 22.5px; letter-spacing: 0.8px;
  }
  .address .accent { color: var(--orange); }
  .base-band {
    left: 0; bottom: 0; width: 100%; height: 14px;
    background: var(--orange);
  }

  .legal {
    left: 0; top: 240px; width: 100%;
    text-align: center;
    font-family: "Montserrat", sans-serif;
    font-weight: 500; font-size: 15.5px;
    line-height: 15.6px; letter-spacing: 1.4px;
    color: var(--ink);
  }
  .partner-badge { left: 46px; top: 326px; }
  .partner-guild {
    left: 526px; top: 360px;
    display: flex; align-items: center; gap: 12px;
  }
  .partner-guild span {
    font-weight: 900; font-size: 19px; color: var(--navy); letter-spacing: 0.5px;
  }
</style>
</head>
<body>

<section class="card card--front">
  <svg class="deco-ring" width="460" height="460" viewBox="0 0 460 460" aria-hidden="true">
    <circle cx="230" cy="230" r="217" fill="none" stroke="var(--faint-grey)" stroke-width="25"/>
  </svg>

  <svg class="brand-ring front-brand-ring" width="148" height="148" viewBox="0 0 148 148" aria-hidden="true">
    <circle cx="74" cy="74" r="69" fill="none" stroke="var(--grey)" stroke-width="7"/>
  </svg>
  <div class="brand-name front-brand-name">Kin<br>Venture<br>Advisory</div>

  <h1 class="abs holder-name">Greg Holloway</h1>
  <p class="abs holder-role">Director</p>
  <div class="abs divider"></div>

  <ul class="abs contact-list">
    <li>
      <svg viewBox="0 0 16 16" aria-label="Phone"><rect x="4" y="1" width="8" height="14" rx="1.5" fill="none" stroke="var(--orange)" stroke-width="1.6"/><line x1="6.5" y1="12.5" x2="9.5" y2="12.5" stroke="var(--orange)" stroke-width="1.4"/></svg>
      08-9342-5817
    </li>
    <li>
      <svg viewBox="0 0 16 16" aria-label="Mobile"><path d="M11 1.5 L8.5 4 C6 6.5 5 10 6 14.5 L8 14 L9 11 L7.8 10.2 C7.5 8 8 6.5 9.5 5 L11 6 L13 3.5 Z" fill="var(--orange)"/></svg>
      0431-587-209
    </li>
    <li class="email">
      <svg viewBox="0 0 16 16" aria-label="Email"><rect x="1" y="3.5" width="14" height="9" fill="none" stroke="var(--orange)" stroke-width="1.5"/><path d="M1 3.5 L8 9 L15 3.5 M1 12.5 L6 7.5 M15 12.5 L10 7.5" fill="none" stroke="var(--orange)" stroke-width="1.3"/></svg>
      greg@kinventureadvisory.com.au
    </li>
    <li>
      <svg viewBox="0 0 16 16" aria-label="Website"><circle cx="8" cy="8" r="6.5" fill="none" stroke="var(--orange)" stroke-width="1.4"/><path d="M4 5 C6 4 7 6 6 8 C5 10 8 11 9 13 M10 3 C11 5 13 6 13.5 8" fill="none" stroke="var(--orange)" stroke-width="1.6"/></svg>
    </li>
  </ul>

  <address class="abs address">
    Unit4,15 Kestrel Lane,<br>
    Carrow Bay,WA,6297<br>
    www.<span class="accent">kinventureadvisory</span>.com.au
  </address>

  <div class="abs base-band"></div>
</section>

<section class="card card--back">
  <svg class="brand-ring back-brand-ring" width="148" height="148" viewBox="0 0 148 148" aria-hidden="true">
    <circle cx="74" cy="74" r="69" fill="none" stroke="var(--grey)" stroke-width="7"/>
  </svg>
  <div class="brand-name back-brand-name">Kin<br>Venture<br>Advisory</div>

  <p class="abs legal">
    ABN:47 219 583 906<br>
    Licensed Real Estate &amp;Business&nbsp; Agent No.RA53174<br>
    QTN&nbsp; Licensee Services Pty Ltd<br>
    AFSL No.527361
  </p>

  <svg class="abs partner-badge" width="98" height="98" viewBox="0 0 98 98" role="img" aria-label="Accredited adviser badge">
    <circle cx="49" cy="49" r="47" fill="none" stroke="var(--navy)" stroke-width="2.5"/>
    <circle cx="49" cy="49" r="34" fill="none" stroke="var(--navy)" stroke-width="1.5"/>
  </svg>

  <div class="abs partner-guild">
    <svg width="34" height="34" viewBox="0 0 34 34" aria-hidden="true"><circle cx="17" cy="17" r="16" fill="var(--teal)"/></svg>
    <span>Business Broker Guild</span>
  </div>
</section>

</body>
</html>
```